Salon and Spa Distributor Business Card

Need a business card. We are are distributor in the salon and spa industry. We identify with natural beauty. Need a card with:
Company Name: Petal Haven"
Title: "President & CEO"
Address
Company Phone number
email
website
Tag Line:" The Professional Salon Source"

Industry/Entity Type

Business

Contact Information for Business Card

Name: Lena Morcott
Title: "President & CEO"
Address: 317 Birchfield Ln, Oakvane, NJ 07481
Company Phone number: 800-463-9152
email: lenamorcott@petalhaven-example.com
website: www.petalhaven-example.com

Requirements
Should not have
• No black backgrounds

```html
<!DOCTYPE html>
<html lang="en">
<head>
<meta charset="utf-8">
<title>Petal Haven – Business Card</title>
<link rel="stylesheet" href="https://fonts.googleapis.com/css2?family=Comfortaa:wght@300&family=Open+Sans:wght@400;600;700&display=swap">
<style>
  :root {
    --page-bg: #ecebe7;
    --card-dark: #163d24;
    --card-light: #ffffff;
    --green-bright: #5cb546;
    --green-soft: #7cc864;
    --green-mid: #3f9a3a;
    --green-deep: #1f7a3a;
    --ink: #1b1b1b;
    --card-w: 520px;
    --card-h: 297px;
  }
  * { box-sizing: border-box; margin: 0; padding: 0; }
  html, body { width: 1200px; height: 900px; overflow: hidden; }
  body {
    background: var(--page-bg);
    font-family: "Open Sans", Arial, sans-serif;
    position: relative;
  }
  .card {
    position: absolute;
    width: var(--card-w);
    height: var(--card-h);
    overflow: hidden;
    box-shadow: 0 10px 28px rgba(0,0,0,.18);
  }
  /* Front */
  .card--front { left: 60px; top: 301px; background: var(--card-dark); }
  .front-brand {
    position: absolute; left: 0; right: 0; top: 74px;
    display: flex; align-items: center; justify-content: center; gap: 16px;
  }
  .brand-dot {
    width: 46px; height: 46px; border-radius: 50%;
    background: var(--green-soft);
  }
  .brand-name {
    font-family: "Comfortaa", "Trebuchet MS", sans-serif;
    font-weight: 300;
    letter-spacing: .5px;
    line-height: 1.2;
  }
  .front-brand .brand-name { font-size: 34px; color: var(--green-soft); }
  .front-rule {
    position: absolute; left: 0; right: 0; top: 190px; height: 9px;
    background: var(--green-bright);
  }
  .tagline {
    position: absolute; left: 0; right: 0; top: 221px;
    text-align: center;
    color: var(--green-soft);
    font-weight: 700; font-size: 15px; letter-spacing: .3px;
  }
  .front-band {
    position: absolute; left: 0; right: 0; bottom: 0; height: 20px;
    background: var(--green-bright);
  }
  /* Back */
  .card--back { left: 620px; top: 301px; background: var(--card-light); }
  .back-brand { position: absolute; left: 30px; top: 26px; }
  .back-brand .brand-name { font-size: 40px; color: var(--green-mid); }
  .holder { position: absolute; left: 44px; top: 104px; }
  .holder-name {
    color: var(--green-mid); font-weight: 600; font-size: 21px; letter-spacing: .4px;
    line-height: 28px;
  }
  .holder-title { color: var(--ink); font-size: 13.5px; line-height: 19px; }
  .contact-list { list-style: none; margin-top: 10px; }
  .contact-item {
    display: flex; align-items: center; gap: 9px;
    color: var(--ink); font-size: 13.5px; line-height: 22px;
  }
  .contact-icon { width: 13px; height: 13px; flex: none; }
  .address { color: var(--ink); font-size: 14px; line-height: 20px; margin-top: 10px; }
  .back-band {
    position: absolute; left: 0; right: 0; bottom: 0; height: 22px;
    background: var(--green-deep);
  }
</style>
</head>
<body>
  <section class="card card--front" aria-label="Business card front">
    <div class="front-brand">
      <span class="brand-dot"></span>
      <span class="brand-name">Petal Haven</span>
    </div>
    <div class="front-rule"></div>
    <p class="tagline">THE PROFESSIONAL SALON SOURCE</p>
    <div class="front-band"></div>
  </section>

  <section class="card card--back" aria-label="Business card back">
    <div class="back-brand"><span class="brand-name">Petal Haven</span></div>
    <div class="holder">
      <h1 class="holder-name">LENA MORCOTT</h1>
      <p class="holder-title">President &amp; CEO</p>
      <ul class="contact-list">
        <li class="contact-item">
          <svg class="contact-icon" viewBox="0 0 16 16" aria-hidden="true"><path fill="#3f9a3a" d="M3.5 1.5l2.2 2.6-1.3 1.6c.9 2 2.4 3.6 4.5 4.6l1.6-1.3 2.7 2.1-1.2 2.6C7 13.7 2.3 9 1.3 3.1z"/></svg>
          <span>800-463-9152</span>
        </li>
        <li class="contact-item">
          <svg class="contact-icon" viewBox="0 0 16 16" aria-hidden="true"><rect x="1" y="3" width="14" height="10" fill="#3f9a3a"/><path d="M1.5 3.5L8 9l6.5-5.5" fill="none" stroke="#fff" stroke-width="1.3"/></svg>
          <span>lenamorcott@petalhaven-example.com</span>
        </li>
        <li class="contact-item">
          <svg class="contact-icon" viewBox="0 0 16 16" aria-hidden="true"><circle cx="8" cy="8" r="7" fill="#3f9a3a"/><path d="M1 8h14M8 1c-3 3-3 11 0 14M8 1c3 3 3 11 0 14" fill="none" stroke="#fff" stroke-width="1"/></svg>
          <span>www.petalhaven-example.com</span>
        </li>
      </ul>
      <p class="address">317 Birchfield Ln, Oakvane, NJ 07481</p>
    </div>
    <div class="back-band"></div>
  </section>
</body>
</html>
```